Customizable Form Generation Website

This will be a place for users to quickly generate numerous forms from a categorized list. As the forms are templates with field variables, the site must be able to substitute ‘real data’ for template variable data. This tool will allow for quick custom forms on-demand.

The landing page is attached. We need the User Experience and User Interface solved for us.

EXAMPLE:
——————————————————————-
Dear {{PatientFirstName}},

Please come back for an examination on {{SelectedDate}} with Doctor {{SelectedProvider}}.

Sincerely,

{{SelectedAuthor}}
——————————————————————-

Coming to the Forms Landing Page, the user will see the forms available to select. The user will then click to select a form.

At some point, the user must resolve the variables in the form. For instance, there are the following variables in the above example: PatientFirstName, SelectedDate, SelectedProvider, and SelectedAuthor. We must give the user a chance to select the values for these variables. Using a dropdown combobox will probably work for most. Getting a date selector will be required if the variable happens to contain the string 'date'.

Is it best to preselect common variables before opening the form, or is it best to dynamically scan the template, then give the user the option to give values to each variable found?

The design must include a way for users to upload additional forms. Forms will most probably be PDF, .DOC, .TXT files. This allows users to develop simple or fancy forms of their choosing., then simply drop them into the site for future use.

The design must include a way for users to create new forms. The form creation tool must present to the user the list of predefined variables like {{PatientLastName}} for easy insertion into the form writer. Anytime "{{}}" are used, developers will recognize that as a variable that needs to be resolved.

The forms will be separated into categories as follows:

OFFICE:
- Letterhead
- Sign-In Sheet
- Fax Cover Sheet
SCHEDULER:
- Appointment Reminder
- Missed Appointment Policy
PATIENT:
- Intake Form
- Patient Discharge
- Return to Work or School
- Excuse Slip
- Consent to Treat a Minor
- Verify Non-Pregnancy
RELEASE:
- Health Information Release Form
- X-Ray Release Form
CERTIFICATES:
- Certificate of Care
- Disability Certificate
INSURANCE:
- Authorization to Bill Insurance
- Assignment Authorization
OTHER:
- Free Massage
- Free Vitamins

The design must include a way to add/customize categories. Categories are for organizing the forms logically.

We welcome ANY questions to help understand the requirements.

Good luck!

Industry/Entity Type

Healthcare

Number of Pages Required

3 page

Requirements
Must have
• Must Follow ORBITAL SCHEMA standards
Nice to have
• Great User Experience. Simple, Fast, Clever.
Should not have
• nothing to add here

```html
<!DOCTYPE html>
<html lang="en">
<head>
<meta charset="utf-8">
<title>Forms select – Release</title>
<link href="https://fonts.googleapis.com/css2?family=Poppins:wght@400;500;600;700&family=Roboto:wght@500&display=swap" rel="stylesheet">
<style>
:root{
  --navy-dark:#04192b;
  --navy:#053a5c;
  --navy-line:#0d4a70;
  --ink:#0a3350;
  --blue:#27a7e0;
  --bg:#f0f4f7;
  --field:#ffffff;
  --muted:#5d6b76;
  --placeholder:#6a7680;
}
*{box-sizing:border-box;margin:0;padding:0}
html,body{width:1200px;height:1064px;overflow:hidden}
body{background:var(--bg);font-family:"Poppins",sans-serif;color:var(--ink);position:relative}

.topbar{position:absolute;left:0;top:0;width:1200px;height:36px;background:var(--navy-dark);color:#fff;display:flex;align-items:center;padding:0 22px;font-family:"Roboto",sans-serif;font-size:11.5px;font-weight:500}
.brand{font-family:"Poppins",sans-serif;font-size:17px;font-weight:600;letter-spacing:-.2px;color:#fff}
.topbar-right{margin-left:auto;display:flex;align-items:center;gap:22px}
.topbar-item{display:flex;align-items:center;gap:6px}

.mainnav{position:absolute;left:0;top:36px;width:1200px;height:62px;background:var(--navy);display:flex}
.nav-item{height:62px;border-right:1px solid var(--navy-line);color:#fff;font-family:"Roboto",sans-serif;font-size:11px;font-weight:500;display:flex;flex-direction:column;align-items:center;justify-content:flex-end;padding-bottom:12px;gap:9px;position:relative}
.nav-item svg{width:22px;height:22px}
.nav-item.active::after{content:"";position:absolute;left:0;right:0;bottom:0;height:4px;background:var(--blue)}

.pagehead{position:absolute;left:0;top:98px;width:1200px;height:122px;background:#fff;border-bottom:1px solid #dfe4e8}
.back{position:absolute;left:22px;top:54px}
.menu-btn{position:absolute;left:48px;top:38px;width:47px;height:47px;border-radius:50%;background:#eef1f4;display:flex;align-items:center;justify-content:center}
.page-title{position:absolute;left:108px;top:44px;font-size:23px;font-weight:600;color:var(--ink)}
.cat-label{position:absolute;right:500px;top:52px;font-size:13px;font-weight:500;color:var(--ink)}
.cat-select{position:absolute;left:714px;top:39px;width:258px;height:45px;border-radius:23px;background:#eef1f4;color:var(--muted);font-size:13.5px;display:flex;align-items:center;padding:0 26px;justify-content:space-between}
.btn{background:var(--blue);color:#fff;font-weight:600;border-radius:23px;display:flex;align-items:center;justify-content:center;letter-spacing:.3px}
.create-btn{position:absolute;left:981px;top:39px;width:197px;height:45px;font-size:13px}

.release-title{position:absolute;left:0;width:1200px;top:292px;text-align:center;font-size:37px;font-weight:700;color:var(--ink)}
.release-sub{position:absolute;left:0;width:1200px;top:344px;text-align:center;font-size:16px;color:var(--muted)}

.section-title{position:absolute;left:94px;font-size:17px;font-weight:600;color:var(--ink)}
.field{position:absolute;height:39px;background:var(--field);border-radius:3px;box-shadow:0 2px 6px rgba(10,50,80,.05);font-size:12.5px;color:var(--placeholder);display:flex;align-items:center;justify-content:space-between;padding:0 22px}

.dropzone{position:absolute;left:658px;top:438px;width:402px;height:481px;background:#fff;border:2px dashed #d3d8dc;border-radius:6px;box-shadow:0 14px 30px rgba(10,50,80,.06)}
.drop-title{position:absolute;left:0;width:100%;top:237px;text-align:center;font-size:20px;font-weight:600;color:var(--ink)}
.drop-or{position:absolute;left:0;width:100%;top:274px;text-align:center;font-size:13px;font-weight:600;color:#a9b1b8}
.browse-btn{position:absolute;left:122px;top:303px;width:152px;height:45px;font-size:15px;font-weight:700}

.footer-line{position:absolute;left:22px;top:1003px;width:1156px;height:2px;background:#dde2e6}
.copyright{position:absolute;left:0;width:1200px;top:1026px;text-align:center;font-size:12px;font-weight:500;color:var(--ink);letter-spacing:.2px}
</style>
</head>
<body>

<header class="topbar">
  <div class="brand">CareLedger</div>
  <div class="topbar-right">
    <div class="topbar-item">
      <svg width="18" height="18" viewBox="0 0 18 18" fill="none" stroke="#fff" stroke-width="1.3"><rect x="3" y="2" width="9" height="15"/><rect x="12" y="7" width="4" height="10"/><path d="M5 5h1M8 5h1M5 8h1M8 8h1M5 11h1M8 11h1M5 14h1M8 14h1"/></svg>
      SAMPLE HEALTHCARE PRACTICE
    </div>
    <div class="topbar-item">
      <svg width="14" height="16" viewBox="0 0 14 16" fill="#fff"><circle cx="7" cy="4.5" r="3.8"/><path d="M0 16c0-4 3-6.5 7-6.5s7 2.5 7 6.5z"/></svg>
      WELCOME BACK, TEST
      <svg width="18" height="16" viewBox="0 0 18 16" fill="none" stroke="#fff" stroke-width="2" style="margin-left:8px"><path d="M7 2H2v12h5"/><path d="M6 8h9M11 4l4 4-4 4" fill="#fff"/></svg>
    </div>
  </div>
</header>

<nav class="mainnav">
  <div class="nav-item" style="width:83px"><svg viewBox="0 0 22 22" fill="#c9d6e0"><path d="M11 2 1 11h3v9h5v-6h4v6h5v-9h3z"/></svg>HOME</div>
  <div class="nav-item" style="width:80px"><svg viewBox="0 0 22 22" fill="none" stroke="#c9d6e0" stroke-width="1.5"><rect x="3" y="4" width="16" height="15"/><path d="M3 8h16M7 2v4M15 2v4M6 11h2M10 11h2M14 11h2M6 14h2M10 14h2M14 14h2"/></svg>SCHEDULER</div>
  <div class="nav-item" style="width:75px"><svg viewBox="0 0 22 22" fill="none" stroke="#c9d6e0" stroke-width="1.5"><circle cx="11" cy="7" r="4"/><path d="M4 20c0-5 3-7 7-7s7 2 7 7z"/></svg>PATIENTS</div>
  <div class="nav-item" style="width:90px"><svg viewBox="0 0 22 22" fill="none" stroke="#c9d6e0" stroke-width="1.5"><rect x="3" y="5" width="14" height="15"/><path d="M6 9h8M6 12h8M6 15h8"/><circle cx="17" cy="5" r="3" fill="#c9d6e0"/></svg>ENCOUNTERS</div>
  <div class="nav-item" style="width:75px"><svg viewBox="0 0 22 22" fill="none" stroke="#c9d6e0" stroke-width="1.8"><path d="M11 2v18M15 6c-1-1.5-2.5-2-4-2-2.5 0-4 1.3-4 3s1.5 2.5 4 3 4 1.5 4 3.5-1.5 3-4 3c-1.8 0-3.3-.6-4.3-2"/></svg>PAYMENTS</div>
  <div class="nav-item" style="width:75px"><svg viewBox="0 0 22 22" fill="none" stroke="#c9d6e0" stroke-width="1.5"><rect x="3" y="5" width="14" height="15"/><path d="M6 9h8M6 12h8M6 15h8"/><circle cx="17" cy="5" r="3" fill="#c9d6e0"/></svg>BILLING</div>
  <div class="nav-item" style="width:79px"><svg viewBox="0 0 22 22" fill="none" stroke="#c9d6e0" stroke-width="1.5"><path d="M3 19h17M5 19v-5M9 19v-7M13 19v-5M17 19V8M4 12l5-5 4 3 6-7M15 3h4v4"/></svg>REPORTING</div>
  <div class="nav-item" style="width:81px"><svg viewBox="0 0 22 22" fill="none" stroke="#c9d6e0" stroke-width="1.5"><circle cx="10" cy="12" r="8"/><circle cx="10" cy="12" r="4"/><path d="M10 12 19 3M16 3h3v3"/></svg>MARKETING</div>
  <div class="nav-item active" style="width:75px"><svg viewBox="0 0 22 22" fill="none" stroke="#c9d6e0" stroke-width="1.5"><rect x="5" y="3" width="12" height="17"/><path d="M8 7h6M8 10h6M8 13h6M8 16h6"/></svg>FORMS</div>
  <div class="nav-item" style="width:75px"><svg viewBox="0 0 22 22" fill="#c9d6e0"><rect x="2" y="4" width="3" height="2.5"/><rect x="7" y="4" width="13" height="2.5"/><rect x="2" y="9" width="3" height="2.5"/><rect x="7" y="9" width="13" height="2.5"/><rect x="2" y="14" width="3" height="2.5"/><rect x="7" y="14" width="13" height="2.5"/></svg>LISTS</div>
  <div class="nav-item" style="width:75px"><svg viewBox="0 0 22 22" fill="none" stroke="#c9d6e0" stroke-width="2.6"><circle cx="11" cy="11" r="6" stroke-dasharray="3 2.2"/><circle cx="11" cy="11" r="2.5" stroke-width="1.6"/></svg>ADMIN</div>
</nav>

<section class="pagehead">
  <svg class="back" width="10" height="14" viewBox="0 0 10 14" fill="none" stroke="#0a3350" stroke-width="2"><path d="M8 1 2 7l6 6"/></svg>
  <div class="menu-btn">
    <svg width="24" height="20" viewBox="0 0 24 20" fill="none" stroke="#0a3350" stroke-width="2" stroke-linecap="round"><path d="M8 2h15M1 10h22M8 18h15"/></svg>
  </div>
  <h1 class="page-title">Forms select</h1>
  <div class="cat-label">Select Form Categories:</div>
  <div class="cat-select">Release categories
    <svg width="10" height="7" viewBox="0 0 10 7" fill="none" stroke="#0a3350" stroke-width="1.6"><path d="m1 1 4 4 4-4"/></svg>
  </div>
  <div class="btn create-btn">CREATE NEW FORMS</div>
</section>

<h2 class="release-title">Release</h2>
<p class="release-sub">Health Information Release, X-Ray Release Form</p>

<h3 class="section-title" style="top:400px">Health Information Release Form</h3>
<div class="field" style="left:95px;top:440px;width:251px">Patient name</div>
<div class="field" style="left:359px;top:440px;width:251px">Previous last name (if any)</div>
<div class="field" style="left:95px;top:492px;width:515px">Street address</div>
<div class="field" style="left:95px;top:545px;width:251px">Date of birth
  <svg width="13" height="13" viewBox="0 0 13 13" fill="none" stroke="#0a3350" stroke-width="1.2"><rect x="1" y="2" width="11" height="10"/><path d="M1 5h11M3.5 7h1M6 7h1M8.5 7h1M3.5 9.5h1M6 9.5h1M8.5 9.5h1"/></svg>
</div>
<div class="field" style="left:359px;top:545px;width:251px">City
  <svg width="10" height="7" viewBox="0 0 10 7" fill="none" stroke="#0a3350" stroke-width="1.6"><path d="m1 1 4 4 4-4"/></svg>
</div>
<div class="field" style="left:95px;top:597px;width:122px">State</div>
<div class="field" style="left:224px;top:597px;width:122px;padding-left:13px">Zip code</div>
<div class="field" style="left:359px;top:597px;width:251px">Phone number</div>

<h3 class="section-title" style="top:683px">X-Ray Release Form</h3>
<div class="field" style="left:95px;top:723px;width:515px">Hospital/Clinic/Healthcare Clinician</div>
<div class="field" style="left:95px;top:775px;width:251px">Phone number</div>
<div class="field" style="left:359px;top:775px;width:251px">Fax number</div>
<div class="field" style="left:95px;top:828px;width:515px">Street address</div>
<div class="field" style="left:95px;top:880px;width:251px">City
  <svg width="10" height="7" viewBox="0 0 10 7" fill="none" stroke="#0a3350" stroke-width="1.6"><path d="m1 1 4 4 4-4"/></svg>
</div>
<div class="field" style="left:359px;top:880px;width:122px">State</div>
<div class="field" style="left:488px;top:880px;width:122px;padding-left:14px">Zip code</div>

<div class="dropzone">
  <svg style="position:absolute;left:159px;top:129px" width="84" height="86" viewBox="0 0 84 86">
    <path d="M6 2h46l20 20v56a4 4 0 0 1-4 4H6a4 4 0 0 1-4-4V6a4 4 0 0 1 4-4z" fill="#dde3e8"/>
    <path d="M52 2v20h20z" fill="#a9bcc8"/>
    <path d="M18 44h18M18 52h28M18 60h28" stroke="#a9bcc8" stroke-width="3" stroke-linecap="round"/>
    <circle cx="66" cy="69" r="15" fill="#27a7e0" stroke="#fff" stroke-width="2"/>
    <path d="M66 76V63M60 68l6-6 6 6" fill="none" stroke="#fff" stroke-width="2.6" stroke-linecap="round"/>
  </svg>
  <div class="drop-title">Drag and drop file here</div>
  <div class="drop-or">OR</div>
  <div class="btn browse-btn">BROWSE FILES</div>
</div>

<div class="footer-line"></div>
<footer class="copyright">© COPYRIGHT 2021 CARELEDGER, ALL RIGHTS RESERVED</footer>

</body>
</html>
```